WEBSITE DESIGN, VELTRA paint and panel

We are in need of a website for Veltra Paint & Panel based in Brisbane, Australia. We are a boutique Automotive Paint & Panel Company that provides services to all makes and models of vehicles. We have attached a logo that is still in draft stage but gives you an idea of the colour scheme and fonts and overall impact we are looking for. We are after a white background so this is clean and crisp whilst being sleek, modern and professional. The website must represent our slogan of Flawless shade on the Finest frame. The website must therefore be visually effective as our product is to get colour and placement on vehicle body's correct so the website must have this impact on our clients. We are after a widescreen webpage that is simple and logical to navigate. The final design should give clients the confidence that we can deliver on our promise.
Updates

Target Market(s)

Vehicle Owners who have a need for panel repairs and people who want to reinvigorate their car with a new coat of paint.

Industry/Entity Type

Car Repair

Coding

Coded - Design and coding required

Number of Pages Required

5+ page

Font styles to use
Sans Serif

Colors
ffffff
ffc214
000000

Requirements
Must have
• Page 1 - Home Page
• Page 2 - Our Process
• Page 3 - Private Customers
• Page 4 - Fleet & Corporate
• Page 5 - Insurance
• Page 6 - Get a Quote
• Page 7 - Connect (Contacts Page)
• Same font and colour scheme as the logo.
Should not have
• A typical mechanical/paint and panel layout which looks like a template website.

```html
<!DOCTYPE html>
<html lang="en">
<head>
<meta charset="utf-8">
<title>Veltra Paint &amp; Panel</title>
<link href="https://fonts.googleapis.com/css2?family=Open+Sans:wght@300;400;600;700&display=swap" rel="stylesheet">
<style>
:root{
  --white:#ffffff;
  --gold:#ffc214;
  --gold-deep:#e0a800;
  --black:#000000;
  --ink:#333333;
  --muted:#777777;
  --dark-panel:#2b2b2b;
  --footer-bg:#ededed;
  --line:#d6d6d6;
}
*{margin:0;padding:0;box-sizing:border-box}
html,body{width:841px;height:1200px;overflow:hidden;background:var(--white)}
body{font-family:"Open Sans",sans-serif;color:var(--ink);position:relative}
.abs{position:absolute}

.site-header{left:0;top:0;width:841px;height:62px;background:var(--white)}
.brand{left:86px;top:0;height:62px;display:flex;align-items:center;gap:6px;white-space:nowrap}
.brand-mark{width:10px;height:10px;background:var(--gold);flex:none}
.brand-name{font-weight:700;font-size:11px;color:var(--black);letter-spacing:.3px}
.main-nav{left:300px;top:0;height:62px;display:flex;align-items:center;gap:18px;font-size:9px;white-space:nowrap}
.main-nav a{color:var(--ink);text-decoration:none;padding:22px 0}
.main-nav a.active{color:var(--gold-deep);border-bottom:2px solid var(--gold)}

.hero{left:0;top:62px;width:841px;height:343px;background:linear-gradient(100deg,#9a9a9a 0%,#7d7f82 40%,#c9c9c9 75%,#f1f1f1 100%)}
.hero-title{left:86px;top:268px;font-size:22px;line-height:1.2;color:var(--white);font-weight:400}
.hero-title .accent{color:var(--gold)}
.hero-dots{left:110px;top:370px;display:flex;gap:6px}
.hero-dots span{width:6px;height:6px;border-radius:50%;background:rgba(255,255,255,.6)}
.hero-dots span.on{background:var(--white)}

.tile{top:435px;width:212px;height:112px}
.tile-1{left:86px;background:linear-gradient(135deg,#c8c8c8,#6f7378)}
.tile-2{left:314px;background:radial-gradient(circle at 50% 55%,#b57a2a,#1a1208 70%)}
.tile-3{left:542px;background:linear-gradient(135deg,#e9e9e9,#8f9499)}
.tile-caption{top:556px;font-size:9px;color:var(--ink)}

.welcome-title{left:86px;top:620px;font-size:19px;font-weight:300;color:var(--gold-deep);letter-spacing:.5px}
.welcome-text{left:86px;top:656px;width:440px;font-size:8.5px;line-height:1.6;color:var(--muted)}
.welcome-text p{margin-bottom:10px}

.target{left:86px;top:800px;width:446px;height:150px;background:var(--dark-panel);padding:22px 0 0 112px}
.target h3{font-size:19px;font-weight:300;color:var(--gold);letter-spacing:.5px}
.target p{width:200px;font-size:8px;line-height:1.5;color:#cfcfcf;margin-top:8px}
.target .btn{display:inline-block;margin-top:10px;background:var(--gold);color:var(--black);font-size:7.5px;padding:4px 10px}

.quote{left:545px;top:622px;width:208px;height:373px;background:var(--gold);padding:16px 14px}
.quote h3{font-size:17px;font-weight:400;color:var(--white);letter-spacing:.5px;margin-bottom:18px}
.quote .field{height:22px;border:1px solid rgba(255,255,255,.7);margin-bottom:10px;font-size:8px;color:var(--white);padding:5px 8px}
.quote .field.area{height:90px}
.quote .submit{margin-top:16px;height:24px;background:var(--dark-panel);color:var(--white);font-size:10px;text-align:center;line-height:24px;letter-spacing:.5px}

.site-footer{left:0;top:1010px;width:841px;height:190px;background:var(--footer-bg)}
.foot-col{top:1034px;font-size:8px;line-height:1.75;color:var(--muted)}
.foot-col.links{left:86px}
.foot-col.legal{left:250px}
.foot-col.contact{left:400px}
.foot-col.social{left:585px}
.social-row{display:flex;align-items:center;justify-content:space-between;width:120px;margin-bottom:11px}
.social-row .dot{width:11px;height:11px;border-radius:50%;background:#b5b5b5}
.foot-rule{left:86px;top:1160px;width:666px;height:1px;background:var(--line)}
.copyright{left:86px;top:1168px;width:666px;font-size:7.5px;color:var(--muted);text-align:center}
.page-no{left:730px;top:1168px;font-size:7.5px;color:var(--muted)}
</style>
</head>
<body>

<header class="site-header abs">
  <div class="brand abs"><span class="brand-mark"></span><span class="brand-name">VELTRA paint and panel</span></div>
  <nav class="main-nav abs">
    <a class="active" href="#">Home</a>
    <a href="#">Our Process</a>
    <a href="#">Private Customers</a>
    <a href="#">Fleet &amp; Corporate Insurance</a>
    <a href="#">Get a Quote</a>
    <a href="#">Connect</a>
  </nav>
</header>

<section class="hero abs" role="img" aria-label="Painter in protective suit spray-painting a dark car body in a paint booth"></section>
<h1 class="hero-title abs"><span class="accent">Flawless shade</span><br>on the Finest frame</h1>
<div class="hero-dots abs"><span class="on"></span><span></span><span></span><span></span></div>

<div class="tile tile-1 abs" role="img" aria-label="Smiling woman driving her car"></div>
<div class="tile tile-2 abs" role="img" aria-label="Business figure silhouetted against warm light"></div>
<div class="tile tile-3 abs" role="img" aria-label="Car owner standing beside a vehicle"></div>
<div class="tile-caption abs" style="left:86px">Private Customers</div>
<div class="tile-caption abs" style="left:314px">Fleet &amp; Corporate Insurance</div>
<div class="tile-caption abs" style="left:542px">Vehicle Owners</div>

<h2 class="welcome-title abs">WELCOME TO VELTRA PAINT &amp; PANEL</h2>
<div class="welcome-text abs">
  <p>Veltra Paint &amp; Panel is a boutique workshop in Brisbane that treats every vehicle with the same care, from small dents to full resprays. Our team matches colour by eye and by instrument, then finishes each panel under controlled light so the result sits perfectly with the rest of the body. We work on all makes and models and stand behind every job we deliver.</p>
  <p>From insurance repairs to fleet maintenance, we keep you informed at every step and return your car on time, looking better than the day you bought it.</p>
</div>

<section class="target abs">
  <h3>OUR TARGET CLIENTS</h3>
  <p>Vehicle owners who need panel repairs, and drivers who want to bring their car back to life with a fresh coat of paint.</p>
  <span class="btn">Learn More</span>
</section>

<section class="quote abs">
  <h3>GET THE QUOTE</h3>
  <div class="field">Name</div>
  <div class="field">Email</div>
  <div class="field">Phone</div>
  <div class="field area">Message</div>
  <div class="submit">GET THE QUOTE</div>
</section>

<footer class="site-footer abs"></footer>
<div class="foot-col links abs">Home<br>Our Process<br>Private Customers<br>Fleet &amp; Corporate Insurance<br>Get a Quote<br>Connect</div>
<div class="foot-col legal abs">Terms &amp; Conditions<br>Privacy Policy<br>Legal Notice</div>
<div class="foot-col contact abs">Veltra Paint &amp; Panel<br>18 Kerrin Street<br>Moorooka QLD 4105<br>Brisbane<br>Telephone: +61 7 3000 0000<br>Email: hello@veltrapaint.com.au</div>
<div class="foot-col social abs">
  <div class="social-row"><span>Facelink</span><span class="dot"></span></div>
  <div class="social-row"><span>Chirper</span><span class="dot"></span></div>
  <div class="social-row"><span>WorkNet</span><span class="dot"></span></div>
</div>
<div class="foot-rule abs"></div>
<div class="copyright abs">© 2015 Company Name Ltd Rights Reserved</div>
<div class="page-no abs">01</div>

</body>
</html>
```